Modernise Business Card

Our company has been operating for 10 years. With the start of the new decade we are looking to refresh our business card design. We manufacture a range of industrial product shipping to customers internationally. A copy of our current card, both sides, is attached. We are looking for a mature professional appearance.

```html
<!DOCTYPE html>
<html lang="en">
<head>
<meta charset="utf-8">
<title>Vantrel Business Card</title>
<link rel="stylesheet" href="https://fonts.googleapis.com/css2?family=Montserrat:wght@400;600&display=swap">
<style>
  :root {
    --page: #ecebe8;
    --card-light: #ffffff;
    --card-dark: #28282b;
    --brand-blue: #1aa7e0;
    --ink: #3c3c3e;
  }
  * { box-sizing: border-box; margin: 0; padding: 0; }
  html, body {
    width: 1111px; height: 1200px; overflow: hidden;
    background: var(--page);
    font-family: "Montserrat", sans-serif;
  }
  .card {
    position: absolute;
    width: 724px; height: 403px;
  }
  .card--front { left: 202px; top: 142px; background: var(--card-light); }
  .card--back  { left: 203px; top: 631px; background: var(--card-dark); }

  .brand-name {
    position: absolute;
    font-family: "Montserrat", sans-serif;
    font-weight: 600;
    color: var(--brand-blue);
    letter-spacing: -0.5px;
    line-height: 1;
  }
  .card--front .brand-name { left: 58px; top: 60px; font-size: 66px; }
  .card--back .brand-name  { right: 36px; top: 307px; font-size: 60px; }

  .holder-name {
    position: absolute; left: 60px; top: 307px;
    font-weight: 600; font-size: 33px;
    color: var(--brand-blue); line-height: 1;
  }
  .address {
    position: absolute; right: 61px; top: 174px;
    text-align: right; font-style: normal;
    font-size: 17.5px; line-height: 21px;
    color: var(--ink);
  }
  .contacts {
    position: absolute; right: 61px; top: 252px;
    list-style: none; text-align: right;
    font-size: 17.5px; color: var(--ink);
  }
  .contacts li {
    display: flex; justify-content: flex-end; align-items: center;
    height: 24px; gap: 6px;
  }
  .contacts svg { width: 17px; height: 17px; flex: none; }
</style>
</head>
<body>
  <section class="card card--front">
    <div class="brand-name">Vantrel</div>
    <address class="address">
      2208-5, Lan Qiao Tower 416<br>
      Meiyuan Road, Haishu District<br>
      Harbourton 318200 China
    </address>
    <ul class="contacts">
      <li>(China) +86 155 0274 1966
        <svg viewBox="0 0 24 24" aria-hidden="true"><path fill="var(--brand-blue)" d="M6.6 10.8a15 15 0 0 0 6.6 6.6l2.2-2.2a1 1 0 0 1 1-.25 11.4 11.4 0 0 0 3.6.57 1 1 0 0 1 1 1V20a1 1 0 0 1-1 1A17 17 0 0 1 3 4a1 1 0 0 1 1-1h3.5a1 1 0 0 1 1 1c0 1.25.2 2.45.57 3.6a1 1 0 0 1-.25 1z"/></svg>
      </li>
      <li>(Australia) +61 400 555 812
        <svg viewBox="0 0 24 24" aria-hidden="true"><path fill="var(--brand-blue)" d="M2 9c0-2 4-4 10-4s10 2 10 4v2h-5V9H7v2H2zM6 12h12l2 8H4z"/></svg>
      </li>
      <li>lharlow@vantrelfittings.com
        <svg viewBox="0 0 24 24" aria-hidden="true"><rect x="2" y="5" width="20" height="14" fill="var(--brand-blue)"/><path d="M2 5l10 8 10-8M2 19l7-7M22 19l-7-7" stroke="#fff" stroke-width="1.5" fill="none"/></svg>
      </li>
      <li>www.vantrelfittings.com
        <svg viewBox="0 0 24 24" aria-hidden="true"><circle cx="12" cy="12" r="10" fill="var(--brand-blue)"/><path d="M7 6c2 1 3 3 2 5s1 3 0 5M15 5c-1 2 1 3 3 4M14 14c2 0 3 2 2 5" stroke="#fff" stroke-width="1.6" fill="none"/></svg>
      </li>
    </ul>
    <div class="holder-name">Lewis Harlow</div>
  </section>

  <section class="card card--back">
    <div class="brand-name">Vantrel</div>
  </section>
</body>
</html>
```